New Business Cards for Organic Meat Farm

We need a business card designed for Thornedge Farm, a meat farm in western MA. Our logo uses a hand-drawn woodcut (attached). Our color palette has been simply black and white (shown in notepad and picture of our food truck). While we are based out of western MA, we have ambitions to grow nationally, so our hope is for a classy and memorable card which will be printed on a premium quality stock from a printer like plavix.com.
Target Market(s)
consumers of quality meats, restauranteurs, partnering farms
Industry/Entity Type
Farming and prepared meat products
Contact Information for Business Card
Wendel Ruark, President/Owner, wendel@thornedgefarm.example, mobile: 555-014-2761, phone: 555-019-6083, thornedgefarm.example, facebook: @thornedgefarm, instagram: @thornedgefarmne
Colors
Designer to choose colors to be used in the design.
Look and feel

```html
<!DOCTYPE html>
<html lang="en">
<head>
<meta charset="utf-8">
<title>Thornedge Farm – Business Card</title>
<link href="https://fonts.googleapis.com/css2?family=Josefin+Sans:wght@400;700&display=swap" rel="stylesheet">
<style>
  :root {
    --ink: #111111;
    --card-black: #1c1c1c;
    --paper: #ffffff;
    --backdrop: #e4e2df;
    --rule: #8a8a8a;
    --art-dark: #2a2a2a;
    --art-light: #d9d9d9;
  }
  * { box-sizing: border-box; margin: 0; padding: 0; }
  html, body { width: 1200px; height: 960px; overflow: hidden; }
  body {
    background: var(--backdrop);
    font-family: "Josefin Sans", sans-serif;
    position: relative;
  }
  .card {
    position: absolute;
    width: 700px;
    height: 400px;
    border-radius: 34px;
    box-shadow: 0 12px 30px rgba(0,0,0,0.25);
    overflow: hidden;
  }
  .card--back { left: 110px; top: 50px; background: var(--card-black); color: var(--paper); }
  .card--front { left: 390px; top: 500px; background: var(--paper); color: var(--ink); }

  /* Back: centred brand */
  .back-brand {
    position: absolute; inset: 0;
    display: flex; flex-direction: column; align-items: center; justify-content: center;
    gap: 22px;
  }
  .back-brand .woodcut {
    width: 330px; height: 170px; border-radius: 6px;
    background: linear-gradient(180deg, #5a5a5a 0%, #8c8c8c 55%, #3a3a3a 100%);
  }
  .wordmark {
    font-family: "Josefin Sans", sans-serif;
    font-weight: 700;
    font-size: 40px;
    letter-spacing: 1px;
  }

  /* Front */
  .front-brand {
    position: absolute; left: 36px; top: 90px; width: 270px;
    display: flex; flex-direction: column; align-items: center; gap: 16px;
  }
  .front-brand .woodcut {
    width: 250px; height: 140px; border-radius: 6px;
    background: linear-gradient(180deg, var(--art-light) 0%, #9a9a9a 55%, var(--art-dark) 100%);
  }
  .front-brand .wordmark { font-size: 30px; color: var(--ink); }
  .divider {
    position: absolute; left: 330px; top: 70px; width: 1px; height: 220px;
    background: var(--rule);
  }
  .contact { position: absolute; left: 360px; top: 50px; }
  .contact-name { font-weight: 700; font-size: 30px; letter-spacing: 0.5px; }
  .contact-title { font-size: 17px; margin: 4px 0 12px 14px; }
  .contact-list { list-style: none; }
  .contact-list li {
    display: flex; align-items: center; gap: 10px;
    font-size: 17px; line-height: 30px;
  }
  .contact-list svg { width: 16px; height: 16px; flex: none; }
  .address {
    position: absolute; left: 0; right: 0; bottom: 34px;
    display: flex; align-items: center; justify-content: center; gap: 8px;
    font-size: 17px;
  }
  .address svg { width: 14px; height: 18px; }
</style>
</head>
<body>

<section class="card card--back">
  <div class="back-brand">
    <div class="woodcut" role="img" aria-label="Woodcut illustration of the farmhouse with porch, surrounded by trees"></div>
    <div class="wordmark">Thornedge Farm</div>
  </div>
</section>

<section class="card card--front">
  <div class="front-brand">
    <div class="woodcut" role="img" aria-label="Woodcut illustration of the farmhouse with porch, surrounded by trees"></div>
    <div class="wordmark">Thornedge Farm</div>
  </div>

  <div class="divider"></div>

  <div class="contact">
    <h1 class="contact-name">WENDEL RUARK</h1>
    <p class="contact-title">President/Owner</p>
    <ul class="contact-list">
      <li>
        <svg viewBox="0 0 16 16" aria-hidden="true"><rect x="4" y="1" width="8" height="14" rx="1.5" fill="none" stroke="currentColor" stroke-width="1.3"/><circle cx="8" cy="12.5" r="0.8" fill="currentColor"/></svg>
        555-014-2761
      </li>
      <li>
        <svg viewBox="0 0 16 16" aria-hidden="true"><path d="M2 6c0-2 2-3 6-3s6 1 6 3l-2 1-1-2H5L4 7z" fill="currentColor"/><rect x="3" y="8" width="10" height="6" rx="1" fill="currentColor"/></svg>
        555-019-6083
      </li>
      <li>
        <svg viewBox="0 0 16 16" aria-hidden="true"><rect x="1" y="3" width="14" height="10" fill="currentColor"/><path d="M1 3l7 6 7-6" fill="none" stroke="#fff" stroke-width="1.2"/></svg>
        wendel@thornedgefarm.example
      </li>
      <li>
        <svg viewBox="0 0 16 16" aria-hidden="true"><circle cx="8" cy="8" r="6.5" fill="none" stroke="currentColor" stroke-width="1.3"/><ellipse cx="8" cy="8" rx="2.8" ry="6.5" fill="none" stroke="currentColor" stroke-width="1.1"/><path d="M1.5 8h13" stroke="currentColor" stroke-width="1.1"/></svg>
        thornedgefarm.example
      </li>
      <li>
        <svg viewBox="0 0 16 16" aria-hidden="true"><rect x="2" y="2" width="12" height="12" rx="2" fill="currentColor"/></svg>
        @thornedgefarm
      </li>
      <li>
        <svg viewBox="0 0 16 16" aria-hidden="true"><circle cx="8" cy="8" r="6" fill="none" stroke="currentColor" stroke-width="1.5"/></svg>
        @thornedgefarmne
      </li>
    </ul>
  </div>

  <p class="address">
    <svg viewBox="0 0 14 18" aria-hidden="true"><path d="M7 1a5.5 5.5 0 0 0-5.5 5.5C1.5 11 7 17 7 17s5.5-6 5.5-10.5A5.5 5.5 0 0 0 7 1z" fill="currentColor"/><circle cx="7" cy="6.5" r="2" fill="#fff"/></svg>
    18 Millbrook Rd, Eastvale, MA 01099
  </p>
</section>

</body>
</html>
```